Halvicek Law Group, PLLC
Business card and stationery
Professional
Marcus T. Halvicek, Esq.
President
248 Perrin Avenue
Suite 3407
New York, New York 10093
mhalvicek@halviceklawgroup.example
www.halviceklawgroup.example
Using Ivory-colored card stock
There are 2 additional staff members that need cards:
nothing

```html
<!DOCTYPE html>
<html lang="en">
<head>
<meta charset="utf-8">
<title>Halvicek Law Group, PLLC — Business Card</title>
<link rel="stylesheet" href="https://fonts.googleapis.com/css2?family=Open+Sans:wght@400;600&display=swap">
<style>
  :root {
    --backdrop: #262626;
    --card: #fdfdfb;
    --maroon: #4f1f1d;
    --band: #5a2422;
    --band-text: #ffffff;
    --ink: #2c2c2c;
  }
  html, body {
    margin: 0;
    padding: 0;
    width: 1200px;
    height: 978px;
    overflow: hidden;
    background: var(--backdrop);
  }
  .business-card {
    position: absolute;
    left: 185px;
    top: 256px;
    width: 830px;
    height: 480px;
    background: var(--card);
    border-radius: 42px;
    overflow: hidden;
    font-family: "Open Sans", sans-serif;
  }
  .firm-name {
    position: absolute;
    left: 0;
    top: 112px;
    width: 100%;
    margin: 0;
    display: flex;
    align-items: center;
    justify-content: center;
    gap: 18px;
    color: var(--maroon);
    font-weight: 600;
    font-size: 40px;
    line-height: 56px;
    letter-spacing: 1px;
    text-transform: uppercase;
  }
  .firm-name .rule {
    display: block;
    width: 48px;
    height: 2px;
    background: var(--maroon);
  }
  .title-band {
    position: absolute;
    left: 0;
    top: 294px;
    width: 100%;
    height: 63px;
    background: var(--band);
    color: var(--band-text);
    font-weight: 600;
    font-size: 28px;
    line-height: 63px;
    text-align: center;
  }
  .title-band .divider { margin: 0 6px; }
  .contact {
    position: absolute;
    left: 0;
    top: 384px;
    width: 100%;
    text-align: center;
    font-style: normal;
    font-size: 19px;
    line-height: 30px;
    color: var(--ink);
  }
  .contact p { margin: 0; }
  .contact b { font-weight: 600; }
</style>
</head>
<body>
  <main class="business-card">
    <h1 class="firm-name">
      <span class="rule"></span>
      <span>Halvicek Law Group, PLLC</span>
      <span class="rule"></span>
    </h1>
    <div class="title-band">Marcus T. Halvicek, Esq <span class="divider">|</span> President</div>
    <address class="contact">
      <p><b>A:</b> 248 Perrin Avenue Suite 3407 New York, New York 10093 | <b>P:</b> 212-555-0146</p>
      <p><b>F:</b> 212-555-0187 | <b>E:</b> mhalvicek@halviceklawgroup.example | <b>W:</b> www.halviceklawgroup.example</p>
    </address>
  </main>
</body>
</html>
```